依頼概要
■依頼の目的/概要
インフルエンザワクチンのポスターを作成して頂きたいです。
クリニック内の待合室に掲示します。

■依頼詳細
A2サイズです。
温かみのある柔らかいデザインをお願いします。
ポスターには、人のイラスト入りでお願いします。イラストはご自身で書いてくださってもいいですし、フリー素材でも構いません。
色合いは当院ホームページを参考にしてください。
当院ホームページ https://temuzeku.com/

記載する内容については、添付ファイルを参照してください。
ロゴデータは当選決定後に送らせて頂きます。

納品は、元データ(aiファイルやpsdファイル)とPNG書き出しでお願いします。

■重視する点
過去・現在までにデザインの経験のある方を希望致します。

その他何かご不明な点がございましたら、お気軽にご質問下さい。
よろしくお願いいたします。

文字が大きく読みやすい、温かみのあるデザインです。

皆さま、この度は当コンペにご参加いただき、誠にありがとうございます。
どれも力作で魅力的で選ぶのが大変でした。
今後ともどうぞよろしくお願いします。

```html
<!DOCTYPE html>
<html lang="ja">
<head>
<meta charset="utf-8">
<title>インフルエンザ予防接種</title>
<link rel="stylesheet" href="https://fonts.googleapis.com/css2?family=M+PLUS+Rounded+1c:wght@500;700;800&display=swap">
<style>
:root{
  --green:#2f9a3c;
  --green-dark:#1f7a2c;
  --green-pale:#e6f3d6;
  --green-soft:#cfe8b4;
  --cream:#fbfdf6;
  --text:#2b2b2b;
  --orange:#f08a00;
  --red:#d0342c;
  --sky:#bfe3f2;
}
*{box-sizing:border-box;margin:0;padding:0}
html,body{width:849px;height:1200px;overflow:hidden}
body{font-family:"M PLUS Rounded 1c",sans-serif;color:var(--text);background:var(--cream)}
.poster{position:relative;width:849px;height:1200px;overflow:hidden;background:linear-gradient(#f1f8e6,#fbfdf6 40%)}
.title{position:absolute;left:40px;top:18px;width:769px;height:160px;border:6px solid var(--green);border-radius:28px;background:var(--green-pale);text-align:center;color:var(--green);font-weight:800;line-height:1.05;padding-top:10px}
.title .line1{font-size:68px;letter-spacing:2px}
.title .line2{font-size:64px;letter-spacing:6px}
.notes{position:absolute;left:48px;top:196px;width:760px;list-style:none;font-size:21px;font-weight:700;line-height:1.55}
.notes li{padding-left:24px;text-indent:-24px}
.notes li::before{content:"■";color:var(--green);margin-right:2px}
.illustration{position:absolute;left:90px;top:400px;width:670px;height:318px;border-radius:20px 20px 0 0;background:linear-gradient(180deg,var(--sky),#e8f4d8 60%,#f7e2c4)}
.start{position:absolute;left:590px;top:400px;transform:rotate(-28deg);transform-origin:left bottom;color:var(--orange);font-weight:800;font-size:17px;white-space:nowrap;line-height:30px}
.start b{font-size:22px}
.fees{position:absolute;left:30px;top:728px;width:789px;border-collapse:collapse;font-weight:700}
.fees td{border-top:3px solid var(--green);border-bottom:3px solid var(--green);vertical-align:middle}
.fees .age{width:150px;background:var(--green);color:#fff;font-size:20px;padding:10px 10px;line-height:1.3;border-bottom:3px solid #fff;white-space:nowrap}
.fees .cond{width:240px;background:var(--green-soft);font-size:17px;padding:8px 14px}
.fees .cond.small{color:var(--red);font-size:13px;line-height:1.4}
.fees .detail{padding:8px 22px;font-size:22px;line-height:1.6;background:#fff}
.detail .row{display:block}
.detail .label{display:inline-block;width:150px}
.detail .label::before{content:"■";color:var(--green)}
.detail .sub{padding-left:150px;display:block}
.footer{position:absolute;left:0;top:1106px;width:849px;height:94px;border-top:4px solid var(--green);background:#fff;text-align:center;padding-top:8px}
.footer .depts{font-size:13px;color:var(--green-dark)}
.footer .name{display:inline-flex;align-items:center;gap:12px;font-size:40px;font-weight:800;color:var(--green);margin-top:2px}
.footer .mark{width:34px;height:34px;background:var(--green);border-radius:6px}
</style>
</head>
<body>
<div class="poster">
  <header class="title">
    <div class="line1">インフルエンザ</div>
    <div class="line2">予防接種</div>
  </header>

  <ul class="notes">
    <li>インフルエンザに対する抵抗力がつくまで約２週間かかり、<br>その効果は約５ヵ月間持続します。</li>
    <li>２回接種をご希望の方は、１回接種から４週間後に２回目接種を行います。</li>
    <li>肺炎球菌ワクチンと同時接種できます。</li>
    <li>体温が37.5度以上、具合が悪い場合は別の日に接種しましょう。</li>
    <li>当院では妊娠中の方も予防接種できます。</li>
  </ul>

  <div class="illustration" role="img" aria-label="開いた窓から笑顔でのぞく三世代の家族のイラスト"></div>
  <div class="start"><b>10月1日(金)</b>からはじまります。</div>

  <table class="fees">
    <tr>
      <td class="age">65歳以上</td>
      <td class="cond">相模原市公費負担あり</td>
      <td class="detail" rowspan="2">
        <span class="row"><span class="label">接種費用</span>¥1,500</span>
        <span class="row"><span class="label">接種回数</span>1回</span>
        <span class="row"><span class="label">期　　間</span>10月1日〜12月31日</span>
      </td>
    </tr>
    <tr>
      <td class="age">60歳以上<br>65歳未満</td>
      <td class="cond small">心臓・腎臓・肺に障害がある方<br>HIV感染による免疫低下の方<br>※詳しくはお問い合わせください</td>
    </tr>
    <tr>
      <td class="age">上記以外の方<br>13歳以上<br>65歳未満</td>
      <td class="cond"></td>
      <td class="detail">
        <span class="row"><span class="label">接種費用</span>¥4,000(1回目)</span>
        <span class="sub">(¥3,000(2回目))</span>
        <span class="row"><span class="label">期　　間</span>10月1日〜</span>
      </td>
    </tr>
  </table>

  <footer class="footer">
    <div class="depts">内科／呼吸器内科／循環器内科／消化器内科</div>
    <div class="name"><span class="mark"></span>桜木内科クリニック</div>
  </footer>
</div>
</body>
</html>
```